Harmony Swift Care Business card

We want a business card that matches our business theme. Our website is www.swiftcarehub.example
The company name is Harmony Swift Care
The persons having the business cards will be doctors
My logo is attached.
We have a drive-thru medical center where our motto is Fast, Reliable, and Convenient. Our goal is to change the medical space while utilizing technologies, keeping a professional and clean look

Medical

Info on the card should be: Name, Position, Cell number, website, email address, possibly the office line as well

Requirements
Must have
• Logo
Nice to have
• Professional medical feel with our logo colors incorporated

```html
<!DOCTYPE html>
<html lang="en">
<head>
<meta charset="utf-8">
<title>Harmony Swift Care – Business Card</title>
<link href="https://fonts.googleapis.com/css2?family=Jost:wght@400;500;600;700&display=swap" rel="stylesheet">
<style>
  :root {
    --brand-blue: #1b479b;
    --sky-blue: #3fb8ec;
    --ink: #111111;
    --card-white: #f4f4f5;
    --card-grey: #dcdcde;
    --mark-faint: rgba(150, 160, 205, 0.35);
    --stage: #e9ebee;
  }
  * { box-sizing: border-box; margin: 0; padding: 0; }
  html, body {
    width: 1200px; height: 1000px; overflow: hidden;
    background: var(--stage);
    font-family: "Jost", sans-serif;
  }
  .card-pair {
    position: absolute; top: 341px; left: 28px;
    display: flex; gap: 34px;
  }
  .card {
    position: relative; width: 556px; height: 318px; overflow: hidden;
  }
  .card-back {
    background: var(--brand-blue);
    display: flex; align-items: center; justify-content: center; gap: 18px;
  }
  .card-back .brand-dot {
    width: 58px; height: 58px; border-radius: 50%;
    border: 10px solid #ffffff;
  }
  .card-back .brand-name {
    color: #ffffff; font-weight: 600; font-size: 34px; line-height: 1.1;
  }
  .card-front {
    background: radial-gradient(circle at 30% 40%, #ffffff 0%, var(--card-white) 45%, var(--card-grey) 100%);
  }
  .faint-disc {
    position: absolute; right: -70px; top: 100px;
    width: 260px; height: 260px; border-radius: 50%;
    background: var(--mark-faint);
  }
  .brand-lockup { position: absolute; left: 42px; top: 36px; }
  .brand-row { display: flex; align-items: center; gap: 10px; }
  .brand-row .brand-name {
    color: var(--brand-blue); font-weight: 600; font-size: 22px;
  }
  .brand-row .brand-dot {
    width: 34px; height: 34px; border-radius: 50%;
    background: var(--sky-blue);
  }
  .tagline {
    margin-top: 4px; font-size: 8.5px; font-weight: 500;
    letter-spacing: 0.4px; color: var(--ink);
  }
  .holder { position: absolute; left: 44px; top: 134px; }
  .holder-name {
    color: var(--brand-blue); font-weight: 600; font-size: 29px; line-height: 1.1;
  }
  .holder-position {
    color: var(--ink); font-weight: 500; font-size: 29px; line-height: 1.2;
  }
  .contact-list {
    position: absolute; left: 46px; top: 230px; list-style: none;
  }
  .contact-list li {
    display: flex; align-items: center; gap: 8px;
    font-size: 13px; color: var(--ink); height: 21.5px;
  }
  .contact-list svg { width: 14px; height: 14px; fill: var(--brand-blue); }
</style>
</head>
<body>
  <main class="card-pair">
    <section class="card card-back" aria-label="Card back">
      <span class="brand-dot"></span>
      <span class="brand-name">Harmony Swift Care</span>
    </section>

    <section class="card card-front" aria-label="Card front">
      <div class="faint-disc"></div>
      <div class="brand-lockup">
        <div class="brand-row">
          <span class="brand-name">Harmony Swift Care</span>
          <span class="brand-dot"></span>
        </div>
        <p class="tagline">CARE ON YOUR WAY, EVERY DAY</p>
      </div>

      <div class="holder">
        <p class="holder-name">Name</p>
        <p class="holder-position">Position</p>
      </div>

      <ul class="contact-list">
        <li>
          <svg viewBox="0 0 24 24" aria-hidden="true"><path d="M6.6 10.8a15 15 0 0 0 6.6 6.6l2.2-2.2c.3-.3.7-.4 1-.2 1.1.4 2.3.6 3.6.6.6 0 1 .4 1 1V20c0 .6-.4 1-1 1A17 17 0 0 1 3 4c0-.6.4-1 1-1h3.5c.6 0 1 .4 1 1 0 1.3.2 2.5.6 3.6.1.3 0 .7-.2 1z"/></svg>
          +1 (555) 014-2290
        </li>
        <li>
          <svg viewBox="0 0 24 24" aria-hidden="true"><path d="M2 5h20v14H2z M3.5 6.5 12 13l8.5-6.5" fill="none" stroke="#1b479b" stroke-width="2"/></svg>
          info@swiftcarehub.example
        </li>
        <li>
          <svg viewBox="0 0 24 24" aria-hidden="true"><circle cx="12" cy="12" r="9" fill="none" stroke="#1b479b" stroke-width="2"/><path d="M3 12h18M12 3c3 3 3 15 0 18M12 3c-3 3-3 15 0 18" fill="none" stroke="#1b479b" stroke-width="1.6"/></svg>
          swiftcarehub.example
        </li>
      </ul>
    </section>
  </main>
</body>
</html>
```